I need a business card.

I need a simple, minimalist, business card. I think the coolest business card I have ever seen is Marty Vexler's from Kestrel's 9... it is just a little creepy for the real world.
I am a photographer and I need a card that I can give to brides or potential portrait customers that is simple and classy.
My name is Glen Hardesty. My website is www.glenhardesty-example.com
Please design my card.
I think it could be as simple as my name, phone # and website... where the rest of my contact could be found... or maybe my email and no website... I am open to ideas. I imagined the card on thick card stock with a black background...

```html
<!DOCTYPE html>
<html lang="en">
<head>
<meta charset="utf-8">
<title>Glen Hardesty – Business Card</title>
<link href="https://fonts.googleapis.com/css2?family=Comfortaa:wght@700&family=Questrial&display=swap" rel="stylesheet">
<style>
  :root {
    --backdrop: #dcdcdc;
    --card: #030303;
    --card-rule: #262626;
    --ink: #ffffff;
  }
  html, body {
    margin: 0;
    padding: 0;
    width: 1200px;
    height: 873px;
    overflow: hidden;
    background: var(--backdrop);
  }
  .canvas {
    position: relative;
    width: 1200px;
    height: 873px;
  }
  .card {
    position: absolute;
    left: 265px;
    width: 680px;
    height: 388px;
    background: var(--card);
  }
  .card--front { top: 41px; }
  .card--back  { top: 450px; }
  .card__frame {
    position: absolute;
    inset: 24px;
    border: 1px solid var(--card-rule);
  }
  .brand-name {
    position: absolute;
    left: 0;
    right: 0;
    top: 166px;
    margin: 0;
    text-align: center;
    font-family: "Comfortaa", sans-serif;
    font-weight: 700;
    font-size: 56px;
    letter-spacing: 1px;
    word-spacing: 14px;
    color: var(--ink);
    text-transform: lowercase;
  }
  .contact {
    position: absolute;
    top: 178px;
    width: 300px;
    text-align: center;
    color: var(--ink);
  }
  .contact--phone { left: 20px; }
  .contact--web   { left: 345px; }
  .contact__label {
    margin: 0 0 14px;
    font-family: "Comfortaa", sans-serif;
    font-weight: 700;
    font-size: 27px;
    word-spacing: 6px;
    text-transform: lowercase;
  }
  .contact__value {
    margin: 0;
    font-family: "Questrial", sans-serif;
    font-size: 22px;
    letter-spacing: 0.2px;
  }
  .contact--web .contact__value { font-size: 20px; }
</style>
</head>
<body>
<main class="canvas">
  <section class="card card--front">
    <div class="card__frame"></div>
    <h1 class="brand-name">glen hardesty</h1>
  </section>

  <section class="card card--back">
    <div class="card__frame"></div>
    <div class="contact contact--phone">
      <p class="contact__label">phone number</p>
      <p class="contact__value">555.014.2291</p>
    </div>
    <div class="contact contact--web">
      <p class="contact__label">website</p>
      <p class="contact__value">www.glenhardesty-example.com</p>
    </div>
  </section>
</main>
</body>
</html>
```